Fitness competition business needs a card design

I need a professional business card design using my logo. The card will be horizontal with rounded edges.

Target Market(s)

Female fitness competitors

Industry/Entity Type

Fitness

Contact Information for Business Card

Rose-Lynn Darby
Owner
stagevarno.com
555.301.2187
info@stagevarno.com

Font styles to use
Serif

Colors

Designer to choose colors to be used in the design.

Requirements
Must have
• On the back please add the following:
• Figure
• Bikini
• Physique
• Fitness
Nice to have
• Looking for a very sleek design, contemporary and easy to read.
Should not have
• Should not be difficult to read or be too busy

```html
<!DOCTYPE html>
<html lang="en">
<head>
<meta charset="utf-8">
<title>Stage Varno – Business Card</title>
<link rel="stylesheet" href="https://fonts.googleapis.com/css2?family=Open+Sans:wght@400;600;700&display=swap">
<style>
  :root {
    --bg: #d9d9d9;
    --card: #ffffff;
    --ink: #1f1f1f;
    --ink-soft: #3a3a3a;
    --grey: #58595b;
    --red: #e21f26;
    --faint-red: rgba(226, 31, 38, 0.10);
  }
  * { box-sizing: border-box; margin: 0; padding: 0; }
  html, body {
    width: 1200px; height: 750px; overflow: hidden;
    background: var(--bg);
    font-family: "Open Sans", sans-serif;
  }
  .canvas {
    position: relative; width: 1200px; height: 750px;
    display: flex; align-items: center; justify-content: center; gap: 60px;
  }
  .card {
    position: relative; width: 520px; height: 300px;
    background: var(--card); border-radius: 28px; overflow: hidden;
    box-shadow: 0 6px 18px rgba(0,0,0,0.18);
  }

  /* Front */
  .brand {
    position: absolute; top: 34px; right: 36px;
    display: flex; align-items: center; gap: 10px;
  }
  .brand-square { width: 16px; height: 16px; background: var(--grey); }
  .brand-name {
    font-weight: 700; font-size: 22px; letter-spacing: 1.5px;
    color: var(--red); text-transform: uppercase;
  }
  .brand-rule {
    position: absolute; top: 84px; right: 36px; width: 190px; height: 2px;
    background: var(--grey);
  }
  .brand-faint {
    position: absolute; top: 108px; right: 22px;
    font-weight: 700; font-size: 44px; letter-spacing: 2px;
    color: var(--faint-red); text-transform: uppercase;
  }
  .person { position: absolute; top: 118px; left: 36px; }
  .person-name { font-weight: 700; font-size: 22px; color: var(--ink); }
  .person-role { font-size: 16px; color: var(--ink-soft); margin-top: 2px; }
  .divider {
    position: absolute; left: 36px; right: 36px; top: 210px; height: 2px;
    background: var(--red);
  }
  .contacts {
    position: absolute; left: 36px; top: 222px; list-style: none;
    font-size: 12.5px; color: var(--ink); line-height: 20px;
  }
  .contacts li { display: flex; align-items: center; gap: 12px; }
  .contacts svg { width: 14px; height: 14px; fill: var(--ink); }

  /* Back */
  .back {
    display: flex; flex-direction: column; align-items: center; justify-content: center;
  }
  .back-mark { display: flex; align-items: center; gap: 16px; }
  .back-square { width: 40px; height: 40px; background: var(--grey); }
  .back-name {
    font-weight: 700; font-size: 50px; letter-spacing: 3px;
    color: var(--red); text-transform: uppercase;
  }
  .divisions {
    margin-top: 34px; font-size: 17px; color: var(--ink);
    display: flex; gap: 10px; align-items: center;
  }
  .divisions .dot { width: 6px; height: 6px; border-radius: 50%; background: var(--ink); }
</style>
</head>
<body>
<main class="canvas">
  <section class="card front">
    <div class="brand">
      <span class="brand-square"></span>
      <span class="brand-name">Stage Varno</span>
    </div>
    <div class="brand-rule"></div>
    <div class="brand-faint" aria-hidden="true">Stage Varno</div>

    <div class="person">
      <div class="person-name">Rose-Lynn Darby</div>
      <div class="person-role">Founder</div>
    </div>

    <div class="divider"></div>

    <ul class="contacts">
      <li>
        <svg viewBox="0 0 24 24" aria-hidden="true"><path d="M6.6 10.8a15 15 0 0 0 6.6 6.6l2.2-2.2c.3-.3.7-.4 1-.2 1.1.4 2.3.6 3.6.6.6 0 1 .4 1 1V20c0 .6-.4 1-1 1A17 17 0 0 1 3 4c0-.6.4-1 1-1h3.5c.6 0 1 .4 1 1 0 1.3.2 2.5.6 3.6.1.3 0 .7-.2 1z"/></svg>
        555.301.2187
      </li>
      <li>
        <svg viewBox="0 0 24 24" aria-hidden="true"><path d="M2 5h20v14H2zm2 2v.5l8 5 8-5V7l-8 5z"/></svg>
        info@stagevarno.com
      </li>
      <li>
        <svg viewBox="0 0 24 24" aria-hidden="true"><path d="M12 2a7 7 0 0 0-7 7c0 5 7 13 7 13s7-8 7-13a7 7 0 0 0-7-7zm0 9.5A2.5 2.5 0 1 1 12 6.5a2.5 2.5 0 0 1 0 5z"/></svg>
        stagevarno.com
      </li>
    </ul>
  </section>

  <section class="card back">
    <div class="back-mark">
      <span class="back-square"></span>
      <span class="back-name">Stage Varno</span>
    </div>
    <div class="divisions">
      <span>Figure</span><span class="dot"></span>
      <span>Bikini</span><span class="dot"></span>
      <span>Physique</span><span class="dot"></span>
      <span>Fitness</span>
    </div>
  </section>
</main>
</body>
</html>
```